Launching a consulting business

I need a business card to launch a new consulting business. I provide executive level consultation throughout New York state to CEO and ED's who run and manage non-fo-profit corporations who support individuals with intellectual and developmental disabilities. The field is undergoing an evolution from a social model of care to more outcome based strategies. Having expertise in health care, leading a $50M business providing this service and working in the government creating policy I can bring to the Executive and corporations compassion, vision, strategy with a clear understanding of business practices for success. The field is moving to managed care. My background in health care management brings the expertise to create opportunities and possibilities. I currently have three projects I am consulting on - 1. Field expert assisting an accounting firm in the creation of a managed care application to become a managed care company supporting the ID/DD field. I crafted the care management model 2. Strategizing on product line creation to assure an agency is ready with a compendium services supporting the ID/DD field. 3. Facilitating a financial model to assist in predicting costs to render services in ID/DD. Developing and overlaying outcome measures to position agencies for effective marketing.
Quality is my passion and assuring all people live their life's dreams.
I would also like a template for letterhead stationary following what is created with my business card.
I wold like to incorporate a cranberry/sage tartan plaid within the design.

Please note my last name is spelled wrong on the attachment. I also do not want the tartan plaid used covering the entire card. i open to other ideas and suggestions.

Industry/Entity Type

Government

Contact Information for Business Card

Denise M Forbush
Phone - 845-562-7183
Cell phone 845-734-2096
Email address - denisemfor@quillpost.com

```html
<!DOCTYPE html>
<html lang="en">
<head>
<meta charset="utf-8">
<title>Denise M Forbush — Business Card</title>
<link href="https://fonts.googleapis.com/css2?family=Tinos&display=swap" rel="stylesheet">
<style>
  :root {
    --cranberry: #8f2a32;
    --cranberry-light: #a4454b;
    --cranberry-deep: #87222b;
    --paper: #ffffff;
    --ink: #1b1b1b;
    --backdrop: #ece9e6;
  }
  * { margin: 0; padding: 0; box-sizing: border-box; }
  html, body {
    width: 1200px;
    height: 914px;
    overflow: hidden;
    background: var(--backdrop);
    font-family: "Tinos", "Times New Roman", serif;
  }
  .canvas {
    width: 1200px;
    height: 914px;
    display: flex;
    flex-direction: column;
    align-items: center;
    justify-content: center;
    gap: 60px;
  }
  .card {
    position: relative;
    width: 640px;
    height: 366px;
    background: var(--paper);
    box-shadow: 0 6px 18px rgba(0,0,0,0.18);
    overflow: hidden;
  }
  .holder-name {
    color: var(--cranberry);
    font-variant: small-caps;
    letter-spacing: 1px;
    white-space: nowrap;
  }
  .card--front {
    display: flex;
    align-items: center;
    justify-content: center;
  }
  .card--front .holder-name { font-size: 60px; }

  .card--back .identity {
    height: 152px;
    display: flex;
    flex-direction: column;
    align-items: center;
    justify-content: flex-end;
    padding-bottom: 14px;
  }
  .card--back .holder-name { font-size: 50px; line-height: 1; }
  .role-title {
    color: var(--ink);
    font-size: 19px;
    margin-top: 8px;
    letter-spacing: 0.3px;
  }
  .contact-band {
    position: absolute;
    left: 0; right: 0; bottom: 0;
    height: 214px;
    background: linear-gradient(100deg, var(--cranberry-deep) 0%, var(--cranberry-light) 45%, var(--cranberry-deep) 100%);
    display: flex;
    flex-direction: column;
    align-items: center;
    justify-content: center;
    gap: 12px;
    color: var(--paper);
    font-size: 21px;
  }
  .contact-line {
    display: flex;
    align-items: center;
    gap: 14px;
    width: 330px;
  }
  .contact-line svg { width: 22px; height: 18px; flex: none; }
  .contact-line--email { font-variant: small-caps; letter-spacing: 0.5px; font-size: 20px; }
</style>
</head>
<body>
  <main class="canvas">
    <section class="card card--front">
      <h1 class="holder-name">Denise M Forbush</h1>
    </section>

    <section class="card card--back">
      <div class="identity">
        <h2 class="holder-name">Denise M Forbush</h2>
        <p class="role-title">Executive Business Strategy Consultant</p>
      </div>
      <div class="contact-band">
        <p class="contact-line">
          <svg viewBox="0 0 22 18" aria-hidden="true"><path d="M2 6 Q11 0 20 6 L18 8 L15 6 L15 4 Q11 3 7 4 L7 6 L4 8 Z M6 9 H16 L18 16 H4 Z" fill="#fff"/><circle cx="11" cy="12.5" r="2" fill="var(--cranberry)"/></svg>
          <span>845-562-7183</span>
        </p>
        <p class="contact-line">
          <svg viewBox="0 0 22 18" aria-hidden="true"><rect x="7" y="0.5" width="9" height="17" rx="1.5" fill="none" stroke="#fff" stroke-width="1.4"/><rect x="8.8" y="2.5" width="5.4" height="5" fill="#fff"/><g fill="#fff"><rect x="8.8" y="9.5" width="1.4" height="1.2"/><rect x="10.8" y="9.5" width="1.4" height="1.2"/><rect x="12.8" y="9.5" width="1.4" height="1.2"/><rect x="8.8" y="12" width="1.4" height="1.2"/><rect x="10.8" y="12" width="1.4" height="1.2"/><rect x="12.8" y="12" width="1.4" height="1.2"/></g></svg>
          <span>845-734-2096</span>
        </p>
        <p class="contact-line contact-line--email">
          <svg viewBox="0 0 22 18" aria-hidden="true"><rect x="1" y="2" width="20" height="14" fill="#fff"/><path d="M1 2 L11 10 L21 2 M1 16 L8 8 M21 16 L14 8" fill="none" stroke="var(--cranberry)" stroke-width="1.1"/></svg>
          <span>denisemfor@quillpost.com</span>
        </p>
      </div>
    </section>
  </main>
</body>
</html>
```